KVRo Business Cards

We need a business card design. We are a Technology (Audio Visual) design, sales and installation company. Looking for a double sided design, clean

Contact Information for Business Card

Clean, modern look, 2 sided

Font styles to use
Sans Serif

```html
<!DOCTYPE html>
<html lang="en">
<head>
<meta charset="utf-8">
<title>KVRo Business Card</title>
<link href="https://fonts.googleapis.com/css2?family=Open+Sans:wght@400;700&family=Teko:wght@500&display=swap" rel="stylesheet">
<style>
  :root {
    --brand-orange: #f39422;
    --card-white: #ffffff;
    --ink-navy: #16283a;
    --text-grey: #7a7a7a;
    --backdrop: #262626;
  }
  * { margin: 0; padding: 0; box-sizing: border-box; }
  html, body { width: 1200px; height: 900px; overflow: hidden; }
  body {
    background: var(--backdrop);
    display: flex;
    flex-direction: column;
    align-items: center;
    justify-content: center;
    gap: 40px;
    font-family: "Open Sans", sans-serif;
  }
  .card {
    width: 700px;
    height: 400px;
    position: relative;
  }
  .card-front {
    background: var(--brand-orange);
    display: flex;
    align-items: center;
    justify-content: center;
  }
  .brand-name {
    color: var(--card-white);
    font-family: "Open Sans", sans-serif;
    font-weight: 700;
    font-size: 96px;
    letter-spacing: -2px;
    line-height: 1;
    margin-left: 150px;
    margin-bottom: 50px;
  }
  .card-back {
    background: var(--card-white);
  }
  .back-details {
    position: absolute;
    left: 50px;
    right: 40px;
    bottom: 60px;
    display: flex;
    align-items: center;
  }
  .person-name {
    font-family: "Teko", sans-serif;
    font-weight: 500;
    font-size: 36px;
    color: var(--ink-navy);
    text-transform: uppercase;
    letter-spacing: 0.5px;
    line-height: 1;
    white-space: nowrap;
    padding-right: 26px;
  }
  .divider {
    width: 2px;
    height: 74px;
    background: var(--brand-orange);
  }
  .contact-list {
    list-style: none;
    padding: 0 26px 0 22px;
  }
  .contact-item {
    display: flex;
    align-items: center;
    gap: 10px;
    font-size: 17px;
    line-height: 26px;
    color: var(--text-grey);
    white-space: nowrap;
  }
  .contact-icon {
    width: 16px;
    height: 16px;
    flex: none;
  }
  .web-accent { color: var(--brand-orange); }
  .address {
    font-style: normal;
    font-size: 17px;
    line-height: 26px;
    color: var(--text-grey);
    padding-left: 26px;
    white-space: nowrap;
  }
</style>
</head>
<body>
  <section class="card card-front">
    <span class="brand-name">KVRo</span>
  </section>

  <section class="card card-back">
    <div class="back-details">
      <h1 class="person-name">Dana Whitlock</h1>
      <span class="divider"></span>
      <ul class="contact-list">
        <li class="contact-item">
          <svg class="contact-icon" viewBox="0 0 16 16" fill="none" stroke="#f39422" stroke-width="1.3">
            <circle cx="8" cy="8" r="6.5"/>
            <path d="M5.5 5c0 3 2.5 5.5 5.5 5.5l.6-1.3-1.6-.8-.8.8c-1-.5-1.7-1.2-2.2-2.2l.8-.8-.8-1.6z"/>
          </svg>
          (555)214-0386
        </li>
        <li class="contact-item">
          <svg class="contact-icon" viewBox="0 0 16 16" fill="none" stroke="#f39422" stroke-width="1.3">
            <rect x="1.5" y="3.5" width="13" height="9"/>
            <path d="M1.5 3.5 8 9l6.5-5.5"/>
          </svg>
          sales@kvro.tech
        </li>
        <li class="contact-item">
          <svg class="contact-icon" viewBox="0 0 16 16" fill="none" stroke="#f39422" stroke-width="1.3">
            <circle cx="8" cy="8" r="6.5"/>
            <ellipse cx="8" cy="8" rx="3" ry="6.5"/>
            <path d="M1.5 8h13M2.5 5h11M2.5 11h11"/>
          </svg>
          <span>www.<span class="web-accent">kvro</span>.tech</span>
        </li>
      </ul>
      <span class="divider"></span>
      <address class="address">
        1180 Larkspur Ct.<br>
        Suite 100<br>
        Alder Hill, Georgia 30999
      </address>
    </div>
  </section>
</body>
</html>
```